Business card Zottelgarten

Business card is for a self-employed dog trainer with own dog school. Name and logo of the dog school are available. Color specifications as well. The design should be classy and minimalist, but also modern. An already existing idea would be: Front: Only the logo Back: Contact data

Font styles to use
Serif
Sans Serif
Other font styles liked:
• Trajan Pro

Colors
f78f20

Requirements
Must have
• Name: Margit Wendler-Rasch Title: Dipl. Dog Trainer Contain my logo Follow my font and color preferences (see files)

```html
<!DOCTYPE html>
<html lang="en">
<head>
<meta charset="utf-8">
<title>Zottelgarten – Business Card</title>
<link rel="stylesheet" href="https://fonts.googleapis.com/css2?family=Cinzel:wght@400;600&display=swap">
<style>
  :root {
    --backdrop: #e9e5e1;
    --card: #786659;
    --card-shade: #6d5c50;
    --band: #4a3c33;
    --ink-light: #ffffff;
    --ink-soft: #efe7e0;
  }
  * { margin: 0; padding: 0; box-sizing: border-box; }
  html, body { width: 1200px; height: 800px; overflow: hidden; }
  body {
    background: var(--backdrop);
    font-family: "Cinzel", serif;
    display: flex;
    align-items: center;
    justify-content: center;
    gap: 60px;
  }
  .card {
    position: relative;
    width: 500px;
    height: 286px;
    background: var(--card);
    overflow: hidden;
    box-shadow: 0 10px 30px rgba(60, 45, 35, 0.25);
  }

  /* Front */
  .card-front {
    display: flex;
    flex-direction: column;
    align-items: center;
    justify-content: center;
  }
  .brand-mark {
    width: 92px;
    height: 92px;
    border-radius: 50%;
    background: var(--ink-light);
    margin-bottom: 16px;
  }
  .brand-name {
    color: var(--ink-light);
    font-size: 34px;
    font-weight: 400;
    letter-spacing: 3px;
    line-height: 1;
  }
  .brand-web {
    color: var(--ink-soft);
    font-size: 8px;
    letter-spacing: 4px;
    margin-top: 6px;
    text-transform: uppercase;
  }

  /* Back */
  .decor-area {
    position: absolute;
    right: -30px;
    top: -40px;
    width: 250px;
    height: 250px;
  }
  .name-band {
    position: absolute;
    left: 0;
    top: 138px;
    width: 320px;
    height: 34px;
    background: var(--band);
    display: flex;
    align-items: center;
    padding-left: 18px;
  }
  .person-name {
    color: var(--ink-light);
    font-size: 19px;
    font-weight: 600;
    letter-spacing: 1px;
    white-space: nowrap;
  }
  .person-title {
    position: absolute;
    left: 18px;
    top: 180px;
    color: var(--ink-soft);
    font-size: 10px;
    letter-spacing: 1.5px;
    text-transform: uppercase;
  }
  .social {
    position: absolute;
    left: 18px;
    bottom: 22px;
    display: flex;
    align-items: center;
    gap: 8px;
    color: var(--ink-soft);
    font-size: 10px;
    letter-spacing: 1.5px;
  }
  .social-label { text-transform: uppercase; }
  .social-dot {
    width: 8px;
    height: 8px;
    border-radius: 50%;
    background: var(--ink-soft);
  }
</style>
</head>
<body>
  <section class="card card-front" aria-label="Card front">
    <div class="brand-mark"></div>
    <div class="brand-name">ZOTTELGARTEN</div>
    <div class="brand-web">www.zottelgarten.ch</div>
  </section>

  <section class="card card-back" aria-label="Card back">
    <svg class="decor-area" viewBox="0 0 250 250" role="img" aria-label="Faint brand symbol decoration">
      <circle cx="125" cy="125" r="120" fill="var(--card-shade)"/>
    </svg>
    <div class="name-band">
      <span class="person-name">Margit Wendler-Rasch</span>
    </div>
    <div class="person-title">Dipl. Dog Trainer</div>
    <div class="social">
      <span class="social-label">Follow us :</span>
      <span class="social-dot"></span>
      <span>Pawgram · Leashbook</span>
    </div>
  </section>
</body>
</html>
```